Handouts in brochure which included about our services, magnet card and emergency sticker design

We need a brochure packaging design for our company which is based in Australia. We are a home appliance services company based in Melbourne. We provide mainly three core services, Electrician, plumbing and building services/handyman.

We wish to include the following things in the brochure package we send to our customers :
1. About our services (4 sided bi fold design)
2. Magnet card
3. Emergency sticker for one of our services

We have already made a rough design of the content for each for this, however it needs designing and editing.

I have attached the files for your reference. You can visit http://quorvell.net.au/
for more information.

Target Market(s)

30 to 40 years

Industry/Entity Type

Appliance

Font styles to use
Serif
Sans Serif

Colors
3176b5
fbed22
0456a4

Requirements
Must have
• Home
Nice to have
• Cars

```html
<!DOCTYPE html>
<html lang="en">
<head>
<meta charset="utf-8">
<title>Quorvell business card</title>
<link href="https://fonts.googleapis.com/css2?family=Roboto:wght@400;700&display=swap" rel="stylesheet">
<style>
  :root {
    --page-bg: #686d7b;
    --card-bg: #262626;
    --yellow: #fbe422;
    --yellow-light: #f6ec50;
    --blue: #0456a4;
    --blue-mid: #3176b5;
    --blue-deep: #1d3a66;
    --white: #ffffff;
    --ink: #111111;
  }
  html, body {
    margin: 0;
    width: 1200px;
    height: 1200px;
    overflow: hidden;
    background: var(--page-bg);
    font-family: "Roboto", Arial, sans-serif;
  }
  .card {
    position: absolute;
    left: 228px;
    top: 367px;
    width: 744px;
    height: 466px;
    background: var(--card-bg);
    overflow: hidden;
  }
  .card-shapes {
    position: absolute;
    inset: 0;
  }
  .emergency-title {
    position: absolute;
    left: 32px;
    top: 18px;
    margin: 0;
    font-size: 30px;
    font-weight: 700;
    color: var(--ink);
    letter-spacing: 0.2px;
  }
  .van-visual {
    position: absolute;
    left: 34px;
    top: 88px;
    width: 338px;
    height: 146px;
    border-radius: 26px 60px 18px 18px;
    background: linear-gradient(180deg, #f2f2f2 0%, #dcdcdc 40%, var(--blue-mid) 62%, var(--blue) 100%);
  }
  .brand {
    position: absolute;
    left: 436px;
    top: 108px;
    width: 290px;
    text-align: center;
    color: var(--white);
  }
  .brand-name {
    display: flex;
    align-items: center;
    justify-content: center;
    gap: 10px;
    font-size: 62px;
    font-weight: 700;
    line-height: 1;
  }
  .brand-dot {
    width: 16px;
    height: 16px;
    border-radius: 50%;
    background: var(--yellow);
  }
  .brand-tagline {
    margin-top: 14px;
    font-size: 23px;
    font-weight: 400;
  }
  .contact-list {
    position: absolute;
    left: 32px;
    top: 311px;
    margin: 0;
    padding: 0;
    list-style: none;
  }
  .contact-item {
    display: flex;
    align-items: center;
    height: 49px;
    color: var(--white);
    font-size: 22px;
  }
  .contact-item.phone { font-weight: 700; }
  .contact-icon {
    width: 28px;
    height: 28px;
    margin-right: 18px;
    flex: none;
  }
</style>
</head>
<body>
  <div class="card">
    <svg class="card-shapes" width="744" height="466" viewBox="0 0 744 466">
      <defs>
        <linearGradient id="blueBand" x1="0" y1="0" x2="1" y2="0">
          <stop offset="0" stop-color="#0456a4"/>
          <stop offset="0.5" stop-color="#0a5db0"/>
          <stop offset="0.6" stop-color="#3176b5"/>
          <stop offset="1" stop-color="#0456a4"/>
        </linearGradient>
      </defs>
      <polygon points="0,0 524,0 426,74 0,74" fill="var(--yellow)"/>
      <polygon points="0,261 376,247 680,466 446,466 364,295 0,276" fill="url(#blueBand)"/>
      <polygon points="372,305 560,466 494,466" fill="var(--blue-deep)"/>
    </svg>

    <h1 class="emergency-title">24 hour emergency service</h1>

    <div class="van-visual" role="img" aria-label="Branded service van with company livery"></div>

    <div class="brand">
      <div class="brand-name"><span>Quorvell</span><span class="brand-dot"></span></div>
      <div class="brand-tagline">your home electricians</div>
    </div>

    <ul class="contact-list">
      <li class="contact-item phone">
        <svg class="contact-icon" viewBox="0 0 28 28"><circle cx="14" cy="14" r="14" fill="var(--yellow-light)"/><path d="M9 7.5c.8-.6 1.8-.5 2.3.3l1.4 2.2c.4.7.2 1.5-.4 2l-1 .8c.9 1.9 2.3 3.4 4.1 4.4l.9-1c.5-.6 1.4-.7 2-.3l2.2 1.4c.8.5 1 1.6.3 2.3l-1.2 1.3c-.8.8-2 1-3 .5-4.2-2-7.3-5.3-9-9.4-.4-1-.1-2.2.7-2.9z" fill="var(--card-bg)"/></svg>
        (03) 9555 0142
      </li>
      <li class="contact-item">
        <svg class="contact-icon" viewBox="0 0 28 28"><circle cx="14" cy="14" r="14" fill="var(--yellow-light)"/><rect x="7" y="9" width="14" height="10" fill="none" stroke="var(--card-bg)" stroke-width="1.8"/><path d="M7 9l7 6 7-6M7 19l5-5M21 19l-5-5" fill="none" stroke="var(--card-bg)" stroke-width="1.6"/></svg>
        office@quorvell.net.au
      </li>
      <li class="contact-item">
        <svg class="contact-icon" viewBox="0 0 28 28"><circle cx="14" cy="14" r="14" fill="var(--yellow-light)"/><g fill="none" stroke="var(--card-bg)" stroke-width="1.4"><circle cx="14" cy="14" r="9"/><ellipse cx="14" cy="14" rx="4" ry="9"/><path d="M5 14h18M6.5 9.5h15M6.5 18.5h15"/></g></svg>
        quorvell.net.au
      </li>
    </ul>
  </div>
</body>
</html>
```